I would like an amazing design for a eCommerce website called trekharbor.net.

The logo was designed on PixelGuild and is attached below. Whatever your design - it MUST use this logo. Please don't waste your time designing new logos.

The logo is on both black and white backgrounds as I've not yet made my mind up whether to ditch "cool black" in favour of more "fresh, clean white"! I'd like to look at both options.

Trek Harbor is going to be the first destination of choice for anyone who is bored or frustrated at home and wants a life full of adventure. It will stock outdoor clothing and equipment, training kit, expedition gear, and travel clothing and accessories.

But it is a very cool place to go. A fun and exciting Aladdin's cave full of fantastic adventure kit. We will stock inflatable pack rafts, machetes, hammocks and other expedition gear as well as standard outdoor clothing.

This is NOT a geeky outdoor store selling pac-a-macs and walking poles.

The unique thing is that everything stocked is hand selected by me, Tom Weller, an experienced explorer who became the first person to walk the Amazon in 2010. tomweller.net is my site. I now make TV for Horizon Vision.

There will be items at every price level from "only the best" - absolute top end kit, to "get the job done" - stuff that won't break the bank. Everything stocked works. If it doesn't - I won't sell it.

So although the theme is fun and adventurous I have to have it also feeling like a place of professional, expert advice. A place of substance and depth.

Thanks in advance for all your ideas and designs!

Best
Tom

The designs that I like the best have used jungle images as background wallpaper - possible with a green tint to them so that they really do look like background rather than the focus. The focus should obviously be the kit for sale. The best designs have this on a fresh white or light grey background so that it stands out. I like the main logo being in a black header and footer. But the feel of the site can easily become too dark if too much back is used or if the green background image is too dark. We want adventure and cool - but it has to feel light and professional enough to be accessible by people of all ages. Most websites that are successful are white after all and whilst I'd like to be a bit more adventurous than that we shouldn't over do the darkness!

I'm not really a massive fan of side bars and would hope that whichever site I chose had a mega menu system like Marlow Finch that could navigate quickly and easily to any item intuitively.

Any sliders must be about selling kit not images of me.

Thanks so much to everyone who has submitted designs - there are some VERY cool ones out there at the moment

Best,
Tom

Target Market(s)

The target market is primarily 16 to 50 years old outdoor enthusiasts however I will be selling to older people and kids, male and female, so it can't be too modern, too macho, or too complicated to put anyone off.

Requirements
Must have
• Bold, professional, adventurous feel. Not cluttered but not so minimalist that it looks boring too. I would like to select a few colours and work with them.
• Red for high lighted emphasis. See logo
• Greens/blacks/greys as background.
• Clean menu system. I'm probably going use a tailored version of http://bright-bright.shopbuilder.net with mega menus.
Nice to have
• Some personalisation that makes the site mine. Use of hi res images below as background could work although I am keen for the site to look clean and easy to navigate.
Should not have
• Hundreds of boxes and text and clutter. I want this site to show off the items in a classy manner. This is NOT games depot.com! This is a site where hand selected items are proudly displayed and put together, after a lot of thought.

```html
<!DOCTYPE html>
<html lang="en">
<head>
<meta charset="utf-8">
<title>Desert Pucker Sleeve Shirt – Trek Harbor</title>
<link rel="stylesheet" href="https://fonts.googleapis.com/css2?family=Play:wght@400;700&family=Arimo:wght@400;700&display=swap">
<style>
:root{
  --red:#d0232a;
  --black:#000;
  --ink:#1a1a1a;
  --grey-band:#e6e6e6;
  --rule-grey:#bdbdbd;
  --white:#fff;
  --muted:#8a8a8a;
  --wood-a:#2b2b2b;
  --wood-b:#141414;
}
*{box-sizing:border-box;margin:0;padding:0}
html,body{width:738px;height:1200px;overflow:hidden;background:var(--white)}
body{position:relative;font-family:"Arimo",Arial,sans-serif;color:var(--ink)}
.abs{position:absolute}

/* header */
.site-header{left:0;top:0;width:738px;height:67px;background:linear-gradient(100deg,var(--wood-a),var(--wood-b) 40%,var(--wood-a) 70%,var(--wood-b))}
.brand{text-align:center;color:var(--red);font-family:"Play",Arial,sans-serif;font-weight:700;line-height:1}
.brand .name{font-size:20px;letter-spacing:1px;display:block}
.brand .tag{font-size:7.5px;font-weight:700;display:block;margin-top:3px}
.account{top:33px;right:98px;color:var(--white);font-size:8.5px;font-weight:700;display:flex;gap:14px;align-items:center}
.account svg{width:7px;height:8px;margin-right:2px;vertical-align:-1px}

/* nav */
.main-nav{left:0;top:67px;width:738px;height:32px;background:var(--black);color:var(--white);font-size:8.5px;font-weight:700}
.main-nav span{position:absolute;top:12px}
.main-nav .divider{left:540px;top:6px;width:1px;height:20px;background:#444}
.cart{left:558px;display:flex;align-items:center;gap:4px}
.cart em{font-style:normal;color:var(--red)}

/* product */
.crumb{left:92px;top:129px;font-size:8px}
.page-title{left:92px;top:141px;font-size:19px;font-weight:400;font-family:"Play",Arial,sans-serif}
.rule{height:2px;background:var(--red)}
.product-photo{left:112px;top:238px;width:196px;height:234px;background:radial-gradient(ellipse at center,#e9e2d4 0%,#ddd3c1 55%,var(--white) 72%)}
.vline{width:1px;background:var(--rule-grey)}
.info{left:388px;top:230px;width:240px}
.info .p-name{font-size:8px}
.info .price{font-size:22px;margin-top:6px}
.info ul{list-style:none;margin-top:17px;font-size:7px;line-height:18.4px}
.size-select{margin-top:10px;width:80px;height:13px;border:1px solid #aaa;border-radius:3px;font-size:7.5px;font-weight:700;display:flex;align-items:center;justify-content:space-between;padding:0 5px;background:linear-gradient(#fff,#eee)}
.add-cart{margin-top:15px;width:114px;height:28px;background:var(--red);color:var(--white);font-size:8.5px;display:flex;align-items:center;padding-left:16px;gap:9px}
.share{margin-top:14px;display:flex;gap:12px}
.share span{display:inline-flex;align-items:center;height:14px;border:1px solid #ccc;border-radius:2px;font-size:7px;font-weight:700;padding:0 4px;gap:4px;background:#f7f7f7}
.share b{color:var(--red)}

/* related */
.section-title{left:93px;top:560px;font-size:18px;font-weight:400;font-family:"Play",Arial,sans-serif}
.card{top:640px;width:204px;text-align:center}
.card .photo{height:170px;margin:0 auto}
.card .c-name{font-size:8px;margin-top:16px}
.card .c-line{width:62px;height:2px;background:var(--red);margin:5px auto 0}
.card .c-price{font-size:11px;margin-top:7px}

/* payment band */
.pay-band{left:0;top:896px;width:738px;height:78px;background:var(--red)}
.pay-band h3{position:absolute;left:111px;top:30px;color:var(--white);font-family:"Play",Arial,sans-serif;font-weight:400;font-size:15px}
.methods{position:absolute;left:412px;top:29px;display:flex;gap:8px}
.methods span{width:33px;height:20px;background:var(--white);border-radius:2px;font-size:5.5px;font-weight:700;color:var(--ink);display:flex;align-items:center;justify-content:center;text-align:center;line-height:1;white-space:nowrap}

/* newsletter */
.news-band{left:0;top:974px;width:738px;height:116px;background:var(--grey-band)}
.news-band h4{position:absolute;font-family:"Play",Arial,sans-serif;font-weight:400;font-size:15px}
.news-sub{position:absolute;left:116px;top:47px;font-size:7.5px;font-family:"Play",Arial,sans-serif}
.news-input{position:absolute;left:112px;top:60px;width:205px;height:29px;background:var(--white)}
.news-btn{position:absolute;left:317px;top:60px;width:104px;height:29px;background:var(--red);color:var(--white);font-family:"Play",Arial,sans-serif;font-size:12px;display:flex;align-items:center;justify-content:center}
.socials{position:absolute;left:500px;top:59px;display:flex;gap:4px}
.socials span{width:24px;height:24px;background:var(--white);border-radius:2px;font-size:4.6px;font-weight:700;display:flex;align-items:center;justify-content:center;color:var(--ink)}

/* footer */
.site-footer{left:0;top:1090px;width:738px;height:110px;background:var(--black)}
.footer-brand{position:absolute;left:88px;top:17px;width:232px;height:60px;background:#0a0a0a;padding-top:22px}
.footer-nav span{position:absolute;top:49px;color:var(--white);font-size:8.5px;font-weight:700}
.copyright{position:absolute;left:343px;top:85px;font-size:7px;color:#555;font-weight:700}
.go-top{position:absolute;left:675px;top:0;width:44px;height:36px}
</style>
</head>
<body>

<header class="site-header abs" role="img" aria-label="Dark weathered wood texture"></header>
<div class="brand abs" style="left:262px;top:24px;width:216px">
  <span class="name">TREK HARBOR</span>
  <span class="tag">Everything for a life of adventure - by Tom Weller</span>
</div>
<div class="account abs">
  <span>Sign up</span>
  <span><svg viewBox="0 0 7 8"><rect x="0" y="3.5" width="7" height="4.5" fill="#fff"/><path d="M1.5 3.5V2.3a2 2 0 0 1 4 0v1.2" fill="none" stroke="#fff" stroke-width="1"/></svg>Log in</span>
</div>

<nav class="main-nav abs">
  <span style="left:137px">HOME</span>
  <span style="left:217px">SHOP <svg width="7" height="5" viewBox="0 0 7 5"><path d="M0.8 0.8 3.5 3.6 6.2 0.8" fill="none" stroke="#d0232a" stroke-width="1.5"/></svg></span>
  <span style="left:292px">BLOG</span>
  <span style="left:369px">CONTACT</span>
  <span style="left:463px">ABOUT</span>
  <span class="divider"></span>
  <span class="cart" style="top:10px"><svg width="13" height="11" viewBox="0 0 13 11"><path d="M0 1h2.5l1.8 6h6.5l1.5-4.5H3.5" fill="none" stroke="#d0232a" stroke-width="1.4"/><circle cx="5" cy="9.5" r="1.1" fill="#d0232a"/><circle cx="10" cy="9.5" r="1.1" fill="#d0232a"/></svg>Your Cart: <em>0 items</em></span>
</nav>

<main>
  <div class="crumb abs">HOME » CLOTHING » DESERT PUCKER SLEEVE SHIRT</div>
  <h1 class="page-title abs">DESERT PUCKER SLEEVE SHIRT</h1>
  <div class="rule abs" style="left:92px;top:175px;width:554px"></div>

  <div class="product-photo abs" role="img" aria-label="Cream long-sleeve button-down desert shirt with chest pockets"></div>
  <div class="vline abs" style="left:345px;top:226px;height:255px"></div>

  <section class="info abs">
    <div class="p-name">DESERT PUCKER SLEEVE SHIRT</div>
    <div class="price">$65.00</div>
    <ul>
      <li>- SLIM FIT SHIRT MADE FROM 100% COTTON</li>
      <li>- FEATURES BUTTON DOWN COLLAR</li>
      <li>- ALL OVER PATTERN</li>
      <li>- FEATURES INTERNAL CONTRAST PATTERN</li>
      <li>- FRONT CHEST PATCH POCKET WITH BUTTON CLOSURE</li>
    </ul>
    <div class="size-select">– select size – <span>⬍</span></div>
    <div class="add-cart"><svg width="14" height="12" viewBox="0 0 13 11"><path d="M0 1h2.5l1.8 6h6.5l1.5-4.5H3.5" fill="none" stroke="#fff" stroke-width="1.4"/><circle cx="5" cy="9.5" r="1.1" fill="#fff"/><circle cx="10" cy="9.5" r="1.1" fill="#fff"/></svg>ADD TO CART</div>
    <div class="share">
      <span>Like <small>0</small></span>
      <span>Share <small>0</small></span>
      <span><b>Save</b></span>
    </div>
  </section>

  <h2 class="section-title abs">YOU MAY ALSO LIKE...</h2>
  <div class="rule abs" style="left:92px;top:593px;width:554px"></div>

  <article class="card abs" style="left:62px">
    <div class="photo" role="img" aria-label="Light blue long-sleeve desert shirt" style="width:140px;background:radial-gradient(ellipse,#c7dcee 0%,#b5cde4 55%,#fff 72%)"></div>
    <div class="c-name">DESERT PUCKER SLEEVE SHIRT</div><div class="c-line"></div><div class="c-price">$65.00</div>
  </article>
  <div class="vline abs" style="left:271px;top:643px;height:160px"></div>
  <article class="card abs" style="left:266px">
    <div class="photo" role="img" aria-label="Navy and grey reinforced trekking pants" style="width:80px;background:linear-gradient(#1d2636,#3b4040 70%,#1a1a1a)"></div>
    <div class="c-name">DESERT BLUE PANTS</div><div class="c-line"></div><div class="c-price">$165.00</div>
  </article>
  <div class="vline abs" style="left:475px;top:643px;height:160px"></div>
  <article class="card abs" style="left:475px">
    <div class="photo" role="img" aria-label="Grey and black insulated winter boot" style="width:120px;background:radial-gradient(ellipse at 50% 60%,#4a4a42 0%,#2f2f2c 50%,#fff 72%)"></div>
    <div class="c-name">DESERT BOOT GRAY</div><div class="c-line"></div><div class="c-price">$265.00</div>
  </article>
</main>

<section class="pay-band abs">
  <h3>WE ACCEPT THESE PAYMENT METHODS</h3>
  <div class="methods">
    <span>Vexa</span><span>Mintcard</span><span>Dispatch</span><span>Amerigo</span><span>PalPurse</span><span>Coinvale</span>
  </div>
</section>

<section class="news-band abs">
  <h4 style="left:116px;top:28px">NEWSLETTER</h4>
  <p class="news-sub">Sign up to our newsletter for the latest news and special offers.</p>
  <div class="news-input"></div>
  <div class="news-btn">Subscribe</div>
  <h4 style="left:502px;top:32px">FOLLOW US</h4>
  <div class="socials">
    <span>Facemark</span><span>Chirper</span><span>Pinly</span><span>ViewTube</span><span>Snapflick</span>
  </div>
</section>

<footer class="site-footer abs">
  <div class="footer-brand brand">
    <span class="name">TREK HARBOR</span>
    <span class="tag">Everything for a life of adventure - by Tom Weller</span>
  </div>
  <div class="footer-nav">
    <span style="left:345px">HOME</span>
    <span style="left:413px">SHOP</span>
    <span style="left:475px">BLOG</span>
    <span style="left:534px">CONTACT</span>
    <span style="left:609px">ABOUT</span>
  </div>
  <p class="copyright">COPYRIGHT © 2014 TREK HARBOR. ALL RIGHTS RESERVED. ALL PRICES USD.</p>
  <svg class="go-top" viewBox="0 0 44 36"><path d="M0 0H44V26L22 36 0 26Z" fill="#d0232a"/><text x="22" y="16" text-anchor="middle" fill="#fff" font-size="7" font-weight="700" font-family="Arimo,Arial,sans-serif">GoTop</text></svg>
</footer>

</body>
</html>
```